I m Looking to Demonstrate My Product Features via Design & Elements

My Dear Freinds,

I am looking to demonstrate the following features of my product via design & elements (for my Brindlemart listing)
https://www.brindlemart.example/dp/X72QP4LWZN/ref=kvt_h_3_u

1) Soft Touch - Skin Friendly Silky Soft Lining Inner Brushed Fleece

2) Stretchable - Four-way Stretch for Unrestricted Movement

3) Breathable - Moisture Control Odor Resistant

4) Quick-Drying - Sweat Wicking and Quick Dry Performance

5) Moisture-Wicking - Excellent Mobility and Moisture-Wicking

6) Heat Retention - Excellent Thermal Retention

7) Ultra-Light & Comfortable for Daily Warmth

8) Wonderfully Warm - Extra Layer of Warmth Under Your Clothes,

9) Elastic waistband - For the Pants for a Comfortable Snug Fit

10) Shrinkage Controlled - For lasting size and shape

see attached some examples & ideas

P.S. it shouldn't be exactly the same because these are from my competitors

Target Market(s)

People on Brindlemart who are looking to buy Thermal Underwear

Industry/Entity Type

Womens Clothing

Font styles to use
Serif

Colors

Designer to choose colors to be used in the design.

Requirements
Must have
• Needs to be attractive
Nice to have
• Ok
Should not have
• Ok

```html
<!DOCTYPE html>
<html lang="en">
<head>
<meta charset="UTF-8">
<title>Thermal Wear Features</title>
<link rel="stylesheet" href="https://fonts.googleapis.com/css2?family=Playfair+Display:wght@700&family=Cormorant+Garamond:wght@500&display=swap">
<style>
  :root {
    --ink: #2f2f2f;
    --ink-soft: #3f3f3f;
    --bg-light: #f4f2ee;
    --bg-mid: #d9d6d0;
    --bg-warm: #ece4d6;
    --ring-fill: rgba(255,255,255,0.55);
  }
  * { margin: 0; padding: 0; box-sizing: border-box; }
  html, body { width: 1200px; height: 675px; overflow: hidden; }
  body { font-family: "Cormorant Garamond", serif; color: var(--ink); }
  .canvas {
    position: relative; width: 1200px; height: 675px; overflow: hidden;
    background:
      radial-gradient(circle at 20% 30%, var(--bg-light) 0%, transparent 40%),
      radial-gradient(circle at 80% 70%, var(--bg-warm) 0%, transparent 45%),
      radial-gradient(circle at 70% 15%, #ffffff 0%, transparent 35%),
      linear-gradient(180deg, #e8e6e2 0%, var(--bg-mid) 55%, #e2dfda 100%);
  }
  .lifestyle-photo {
    position: absolute; left: 452px; top: 201px; width: 260px; height: 260px;
    border-radius: 50%;
    background: radial-gradient(circle at 45% 40%, #e6e2dc 0%, #b9bcc4 45%, #3a3a3a 75%, #c98a8e 100%);
  }
  .icons { position: absolute; inset: 0; }
  .feature { position: absolute; white-space: nowrap; }
  .feature h2 {
    font-family: "Playfair Display", serif; font-weight: 700;
    font-size: 20px; line-height: 24px; color: var(--ink); letter-spacing: 0.3px;
  }
  .feature p {
    font-weight: 500; font-size: 17px; line-height: 21px; color: var(--ink-soft); margin-top: 2px; letter-spacing: 0.3px;
  }
  .align-right { text-align: right; transform: translateX(-100%); }
  .align-center { text-align: center; transform: translateX(-50%); }
</style>
</head>
<body>
<main class="canvas">
  <div class="lifestyle-photo" role="img" aria-label="Smiling couple relaxing on a bed wearing thermal base layers"></div>

  <svg class="icons" width="1200" height="675" viewBox="0 0 1200 675" fill="none" stroke="var(--ink)" stroke-width="3" stroke-linecap="round" stroke-linejoin="round">
    <g fill="var(--ring-fill)">
      <circle cx="582" cy="141" r="49"/>
      <circle cx="471" cy="177" r="49"/>
      <circle cx="694" cy="177" r="49"/>
      <circle cx="402" cy="273" r="49"/>
      <circle cx="764" cy="273" r="49"/>
      <circle cx="402" cy="390" r="49"/>
      <circle cx="764" cy="390" r="49"/>
      <circle cx="471" cy="486" r="49"/>
      <circle cx="694" cy="486" r="49"/>
      <circle cx="582" cy="522" r="49"/>
    </g>
    <g class="icon-heat">
      <path d="M576 150 V108 a6 6 0 0 1 12 0 V150"/>
      <circle cx="582" cy="168" r="11" fill="var(--ink)"/>
      <rect x="578" y="125" width="8" height="38" fill="var(--ink)" stroke="none"/>
      <path d="M562 132 q-4 8 0 16 q4 8 0 16 M555 136 q-3 6 0 12 q3 6 0 12 M602 132 q4 8 0 16 q-4 8 0 16 M609 136 q3 6 0 12 q-3 6 0 12" stroke-width="2"/>
    </g>
    <g class="icon-moisture">
      <path d="M455 158 q-14 20 -14 30 a14 14 0 0 0 28 0 q0 -10 -14 -30z" fill="var(--ink)"/>
      <path d="M470 160 q8 -10 20 -10 M476 170 q8 -10 20 -10 M480 180 q8 -10 20 -10" stroke-width="2.5"/>
      <path d="M485 146 l5 4 -5 4 M491 156 l5 4 -5 4 M495 166 l5 4 -5 4" stroke-width="2.5"/>
    </g>
    <g class="icon-stretch">
      <path d="M668 155 q14 14 0 20 q20 4 52 30 q-12 -14 2 -22 q-26 -4 -54 -28z" stroke-width="2.5"/>
      <path d="M690 170 l-14 -16 M676 154 v9 M676 154 h9 M700 186 l14 16 M714 202 v-9 M714 202 h-9" stroke-width="2.5"/>
    </g>
    <g class="icon-breathable">
      <path d="M398 240 q-14 14 0 32 q14 18 -2 36 M406 240 q-14 14 0 32 q14 18 -2 36" stroke-width="2.5"/>
      <path d="M412 252 h-36 l7 -6 M376 252 l7 6 M392 296 h36 l-7 -6 M428 296 l-7 6" stroke-width="2.5"/>
    </g>
    <g class="icon-soft" fill="var(--ink)" stroke="none">
      <path d="M731 258 h32 v9 h-32 a4.5 4.5 0 0 1 0 -9z"/>
      <path d="M737 269 h26 v8 h-26 a4 4 0 0 1 0 -8z"/>
      <path d="M765 257 q18 -4 36 -1 v28 q-14 6 -30 4 q-6 -1 -6 -6 z"/>
      <path d="M767 281 q-10 2 -20 4 a4 4 0 0 0 1 8 q14 0 22 -3 z"/>
    </g>
    <g class="icon-quick">
      <circle cx="404" cy="394" r="32"/>
      <path d="M404 394 h-10 M404 394 l10 -12 M404 368 v6 M430 394 h-6 M404 420 v-6" stroke-width="2.5"/>
      <path d="M377 360 q-9 12 -9 18 a9 9 0 0 0 18 0 q0 -6 -9 -18z" fill="var(--ink)"/>
    </g>
    <g class="icon-elastic">
      <path d="M748 356 q-16 34 0 68 M780 356 q16 34 0 68"/>
      <path d="M735 390 q4 -6 8 0 t8 0 t8 0 t8 0 t8 0 t8 0 t8 0 t8 0" stroke-width="2.5"/>
    </g>
    <g class="icon-shrink">
      <path d="M431 473 h80 q-6 13 0 26 h-80 q6 -13 0 -26z"/>
      <path d="M471 460 v52 M466 466 l5 -6 5 6 M466 506 l5 6 5 -6" stroke-width="2.5"/>
    </g>
    <g class="icon-ultra">
      <path d="M676 514 q0 -40 42 -58 q-4 32 -34 46 z" fill="var(--ink)"/>
      <path d="M672 524 q10 -30 40 -62" stroke-width="2"/>
    </g>
    <g class="icon-warm">
      <path d="M544 528 h76 M544 535 h76"/>
      <path d="M566 526 v-20 M560 512 l6 -7 6 7 M582 526 v-20 M576 512 l6 -7 6 7 M598 526 v-20 M592 512 l6 -7 6 7" stroke-width="2.5"/>
    </g>
  </svg>

  <section class="feature align-center" style="left:582px; top:39px;">
    <h2>HEAT RETENTION</h2>
    <p>EXCELLENT THERMAL RETENTION</p>
  </section>
  <section class="feature align-right" style="left:411px; top:117px;">
    <h2>MOISTURE-WICKING</h2>
    <p>EXCELLENT MOBILITY AND<br>MOISTURE-WICKING</p>
  </section>
  <section class="feature" style="left:754px; top:117px;">
    <h2>STRETCHABLE</h2>
    <p>FOUR-WAY STRETCH FOR<br>UNRESTRICTED MOVEMENT</p>
  </section>
  <section class="feature align-right" style="left:340px; top:239px;">
    <h2>BREATHABLE</h2>
    <p>MOISTURE CONTROL &amp;<br>ODOR RESISTANT</p>
  </section>
  <section class="feature" style="left:826px; top:239px;">
    <h2>SOFT TOUCH</h2>
    <p>SKIN FRIENDLY SILKY SOFT LINING<br>INNER BRUSHED FLEECE</p>
  </section>
  <section class="feature align-right" style="left:340px; top:355px;">
    <h2>QUICK-DRYING</h2>
    <p>SWEAT WICKING &amp;<br>QUICK DRY PERFORMANCE</p>
  </section>
  <section class="feature" style="left:826px; top:355px;">
    <h2>ELASTIC WAISTBAND</h2>
    <p>FOR A COMFORTABLE &amp;<br>SNUG FIT</p>
  </section>
  <section class="feature align-right" style="left:408px; top:464px;">
    <h2>SHRINKAGE CONTROLLED</h2>
    <p>FOR LASTING SIZE &amp; SHAPE</p>
  </section>
  <section class="feature" style="left:756px; top:464px;">
    <h2>ULTRA-LIGHT</h2>
    <p>&amp; COMFORTABLE FOR DAILY WARMTH</p>
  </section>
  <section class="feature align-center" style="left:582px; top:580px;">
    <h2>WONDERFULLY WARM</h2>
    <p>EXTRA LAYER OF WARMTH<br>UNDER YOUR CLOTHES</p>
  </section>
</main>
</body>
</html>
```